Creating the Look and Feel of an Elite Boutique Consulting Practice: Kestrel Advisory

Complete a professional website on Weebly. As part of the site, we are open to a new logo -- we have just launched. We put up a starter website that shows you the content and theme we are going for. But clearly we aren't professional web designers and we need your help. Check out our start at kestreladvisory.com

Target Market(s)

Fortune 500 Clients

Industry/Entity Type

Management Consulting

Logo Text

KESTREL Advisory

Number of Pages Required

4 page

Requirements
Must have
• I've already set us up on Weebly. I'd like to give the selected designer the log-in credentials and have the designer create it on Weebly, so we can maintain it through that service.

```html
<!DOCTYPE html>
<html lang="en">
<head>
<meta charset="utf-8">
<title>Kestrel Advisory</title>
<link href="https://fonts.googleapis.com/css2?family=Open+Sans:wght@400;600&family=Raleway:wght@500;600;700;800&display=swap" rel="stylesheet">
<style>
:root{
  --maroon:#7a0f0f;
  --text:#555;
  --dark:#333;
  --muted:#777;
  --footer-bg:#f1f1f1;
  --line:#e6e6e6;
}
*{box-sizing:border-box;margin:0;padding:0}
html,body{width:826px;height:1200px;overflow:hidden;background:#fff}
body{position:relative;font-family:"Open Sans",sans-serif;color:var(--text)}
.abs{position:absolute}
.site-header{left:0;top:0;width:826px;height:74px;background:#fff;border-bottom:1px solid #ddd}
.brand{left:68px;top:15px;width:134px;height:42px;border:1px solid var(--maroon);display:flex;align-items:center;justify-content:center;gap:6px}
.brand .dot{width:8px;height:8px;background:var(--maroon);border-radius:50%}
.brand span{font-family:"Raleway",sans-serif;font-weight:700;font-size:12px;color:var(--maroon);letter-spacing:.3px}
.nav-item{top:32px;font-size:9px;color:#555;letter-spacing:.2px;white-space:nowrap}
.nav-item.active{color:var(--maroon)}
.search-icon{left:750px;top:33px}
.hero{left:0;top:74px;width:826px;height:368px;background:linear-gradient(180deg,#d9b7a8 0%,#f2c3a3 28%,#c99b8f 48%,#6c6672 68%,#3b3a44 100%)}
.hero-title{left:0;top:200px;width:826px;text-align:center;font-family:"Raleway",sans-serif;font-weight:800;font-size:26px;color:#fff;letter-spacing:.3px}
.hero-sub{left:130px;top:245px;width:566px;text-align:center;font-size:11px;line-height:16px;color:#fff}
.hero-btn{left:342px;top:296px;width:142px;height:36px;background:var(--maroon);color:#fff;font-family:"Raleway",sans-serif;font-weight:700;font-size:11.5px;display:flex;align-items:center;justify-content:center;letter-spacing:.3px}
.hero-arrow{top:244px}
.welcome-title{left:0;top:466px;width:826px;text-align:center;font-family:"Raleway",sans-serif;font-weight:600;font-size:15.5px;color:#444}
.welcome-text{left:140px;top:499px;width:546px;text-align:center;font-size:8.4px;line-height:15px;color:#555}
.welcome-text em{font-style:normal;color:var(--maroon)}
.people-title{left:0;top:565px;width:826px;text-align:center;font-family:"Raleway",sans-serif;font-weight:500;font-size:13px;color:var(--maroon)}
.card{top:604px;width:214px;text-align:center}
.card .photo{width:214px;height:107px;box-shadow:0 6px 8px -4px rgba(0,0,0,.25)}
.card h3{margin-top:12px;font-family:"Raleway",sans-serif;font-weight:600;font-size:15px;color:#555}
.card p{margin:10px auto 0;width:200px;font-size:8.4px;line-height:15px;color:#555;height:45px}
.card .btn{display:inline-block;margin-top:14px;width:57px;height:22px;line-height:22px;background:var(--maroon);color:#fff;font-size:8.4px}
.divider{left:68px;top:869px;width:690px;height:1px;background:var(--line)}
.help-title{left:0;top:893px;width:826px;text-align:center;font-family:"Raleway",sans-serif;font-weight:500;font-size:13px;color:var(--maroon)}
.help-list{left:68px;top:932px;width:360px;font-size:8.4px;line-height:15px;color:#555}
.help-list .item{margin-bottom:15px}
.help-list strong{font-weight:600;color:#222}
.help-btn{left:67px;top:1070px;width:122px;height:22px;background:var(--maroon);color:#fff;font-size:8.6px;display:flex;align-items:center;justify-content:center}
.compass-photo{left:453px;top:933px;width:304px;height:159px;background:radial-gradient(circle at 60% 40%,#d9a96a 0%,#a86a34 45%,#6b3b1b 100%)}
.site-footer{left:0;top:1122px;width:826px;height:78px;background:var(--footer-bg)}
.footer-links{left:67px;top:1144px;font-size:8.6px;color:#777}
.footer-copy{left:67px;top:1165px;font-size:8.2px;color:#777}
.social{top:1149px;width:26px;height:26px;border-radius:50%}
</style>
</head>
<body>
<header class="abs site-header">
  <div class="abs brand"><div class="dot"></div><span>KESTREL Advisory</span></div>
  <nav>
    <span class="abs nav-item active" style="left:378px">HOME</span>
    <span class="abs nav-item" style="left:440px">ABOUT KESTREL</span>
    <span class="abs nav-item" style="left:538px">APPROACH</span>
    <span class="abs nav-item" style="left:626px">TEAM</span>
    <span class="abs nav-item" style="left:690px">CONTACT</span>
  </nav>
  <svg class="abs search-icon" width="9" height="9" viewBox="0 0 9 9"><circle cx="3.7" cy="3.7" r="2.8" fill="none" stroke="#666" stroke-width="1.2"/><line x1="5.8" y1="5.8" x2="8.5" y2="8.5" stroke="#666" stroke-width="1.3"/></svg>
</header>

<section class="abs hero" role="img" aria-label="City skyline at sunset with a tall spire tower on the right"></section>
<h1 class="abs hero-title">LET'S CHART YOUR PATH TO SUCCESS.</h1>
<p class="abs hero-sub">Sed ut perspiciatis unde omnis iste natus error sit voluptatem accusantium doloremque laudantium, totam rem aperiam, eaque ipsa quae ab illo inventore veritatis et quasi architecto beatae</p>
<div class="abs hero-btn">GET STARTED HERE</div>
<svg class="abs hero-arrow" style="left:16px" width="26" height="26" viewBox="0 0 26 26"><circle cx="13" cy="13" r="12" fill="none" stroke="#fff" stroke-width="1.2"/><polyline points="15,8 10,13 15,18" fill="none" stroke="#fff" stroke-width="1.2"/></svg>
<svg class="abs hero-arrow" style="left:782px" width="26" height="26" viewBox="0 0 26 26"><circle cx="13" cy="13" r="12" fill="none" stroke="#fff" stroke-width="1.2"/><polyline points="11,8 16,13 11,18" fill="none" stroke="#fff" stroke-width="1.2"/></svg>

<h2 class="abs welcome-title">WELCOME TO KESTREL ADVISORY</h2>
<p class="abs welcome-text"><em>Purpose-Driven Organizational Change</em> sit voluptatem accusantium doloremque laudantium, totam rem aperiam, eaque ipsa quae ab illo inventore veritatis et quasi architecto beatae vitae dicta sunt explicabo. Nemo enim ipsam voluptatem quia voluptas sit aspernatur aut odit aut fugit, sed quia consequuntur magni dtae vitae dicta sunt explicabo. Nemo enim ipsam voluptatem quia voluolore.</p>
<h3 class="abs people-title">The people of KESTREL ADVISORY are:</h3>

<article class="abs card" style="left:68px">
  <div class="photo" role="img" aria-label="Aerial view of dense city towers" style="background:linear-gradient(180deg,#9a9fae,#6d6a6e 55%,#3e3a3a)"></div>
  <h3>Experienced</h3>
  <p style="width:200px">Over the past three decades, we have deep experience driving organizational transformation in more than 33 countries, for some of the world</p>
  <span class="btn">About</span>
</article>
<article class="abs card" style="left:306px">
  <div class="photo" role="img" aria-label="City skyline at golden hour" style="background:linear-gradient(180deg,#c9a68e,#a9785a 55%,#5c4a44)"></div>
  <h3>Curious</h3>
  <p style="width:196px">Each of the dozens of transformations we've enabled are unique. Our most relevant experience is our ability to listen and learn where you</p>
  <span class="btn">Our Team</span>
</article>
<article class="abs card" style="left:543px">
  <div class="photo" role="img" aria-label="Skyline at dusk beside a stone monument" style="background:linear-gradient(180deg,#e3b497,#9d8583 55%,#4c4b57)"></div>
  <h3>Ready to Hear Your Story</h3>
  <p style="width:176px">Of course the best way to get to know more about us is to contact us, get to know us, and see what you think</p>
  <span class="btn">Contact</span>
</article>

<div class="abs divider"></div>
<h3 class="abs help-title">We help your organization achieve a successful, resilient transformation by:</h3>
<div class="abs help-list">
  <div class="item">We help your organization achieve a successful, resilient transformation by:<br><strong>Where are you going? What will you become? Why change now?</strong></div>
  <div class="item">Embedding routines and practices to ensure the transformation is &nbsp;structurally resilient.<br><strong>How should future work be divided, done and measured?</strong></div>
  <div class="item">Assessing the current state of your organization.<br><strong>Where are you today? What should be protected and preserved? What needs to change?</strong></div>
</div>
<div class="abs help-btn">More about our approach.</div>
<div class="abs compass-photo" role="img" aria-label="Compass resting on rolled antique maps"></div>

<footer class="abs site-footer"></footer>
<div class="abs footer-links">Home | &nbsp; approach. | &nbsp;Kestrel | &nbsp;News &amp; Events | &nbsp;Partners | &nbsp;Conatct</div>
<div class="abs footer-copy">Copyright 2015 KESTREL ADVISORY. &nbsp;All rights reserved. &nbsp;&nbsp;Privacy Policy | Legal Terms</div>
<div class="abs social" style="left:634px;background:#1fb6e6"></div>
<div class="abs social" style="left:667px;background:#c4302b"></div>
<div class="abs social" style="left:700px;background:#1e64b0"></div>
<div class="abs social" style="left:730px;background:#1a6fa3"></div>
</body>
</html>
```